Gutschein für Fotograf
Designer PelaWix hat meinen Geschmack am besten getroffen, ging auf meine Änderungsvorschläge genau ein, und änderte Details zu meiner vollsten Zufriedenheit. Kann ich auf alle Fälle weiter empfehlen.
Zielgruppe
Ich bin Fotograf und suche nach einem Gutschein für meine Arbeiten. Zielgruppen sind Privatpersonen, Pärchenfotos, Hochzeit, Baby usw.
Aufgabenstellung
Der Gutschein sollte zu meiner Homepage passen und auch zu meinen Bildern/ meinem Stil.
Folgendes könnte darauf stehen: (Foto) Gutschein - einzulösen bei - meine Homepage sollte darauf sein - es sollte eine Version mit 50 € sein und eine mit 100€ geben. Mir gefällt wahrscheinlich etwas klassisches besser, aber auch retro/ vintage könnte ich mir gut vorstellen. Vor allem möchte ich aber, dass es weiblich/ feminin wirkt. Ob Bilder von mir auf dem Gutschein von Vorteil sind, kann ich leider nicht einschätzen, aber die Bilder können jederzeit von meiner Homepage zu Testzwecken verwendet werden.

```html
<!DOCTYPE html>
<html lang="de">
<head>
<meta charset="utf-8">
<title>Foto Gutschein – Lukas Brenner</title>
<link rel="stylesheet" href="https://fonts.googleapis.com/css2?family=Cormorant+Garamond:wght@400;500&family=Open+Sans:wght@400&display=swap">
<style>
:root{
  --paper:#ffffff;
  --bg:#ffffff;
  --ink:#1c1c1c;
  --brown:#4a3530;
  --red:#a3131c;
  --pattern:#efeeee;
  --haze:#e6e4e3;
  --shadow:rgba(0,0,0,.18);
  --serif:"Cormorant Garamond", Georgia, serif;
  --sans:"Open Sans", Arial, sans-serif;
}
*{box-sizing:border-box;margin:0;padding:0}
html,body{width:1200px;height:821px;overflow:hidden;background:var(--bg)}
.canvas{position:relative;width:1200px;height:821px;font-family:var(--serif);color:var(--ink)}
.section-label{position:absolute;font-family:var(--sans);font-size:23px;color:#111}
.label-outer{left:51px;top:18px}
.label-inner{left:55px;top:421px}
.page{position:absolute;background:var(--paper);box-shadow:1px 2px 4px var(--shadow)}
.page-outer{left:50px;top:52px;width:243px;height:343px}
.page-inner{left:52px;top:460px;width:241px;height:341px}
.damask{position:absolute;background:linear-gradient(180deg,var(--pattern),#f8f8f8 60%,var(--pattern))}
.page-outer .damask{left:0;top:150px;width:100%;height:193px}
.url-flipped{position:absolute;top:23px;width:100%;text-align:center;font-size:7px;transform:rotate(180deg)}
.voucher-frame{position:absolute;border:1px solid var(--red);border-radius:6px;overflow:hidden;background:var(--paper)}
.page-outer .voucher-frame{left:14px;top:182px;width:215px;height:152px}
.photo-haze{position:absolute;inset:0;background:linear-gradient(180deg,var(--haze) 0%,#fbfbfb 35%,#ffffff 60%,#f0efee 100%)}
.emblem{position:absolute;left:50%;transform:translateX(-50%);text-align:center;color:var(--brown)}
.emblem-rule{position:absolute;left:0;right:0;height:1px;background:var(--brown)}
.ornament{margin:0 auto;border-radius:50%;background:radial-gradient(ellipse,#8d7a75,#c9bfbc 55%,transparent 72%)}
.emblem-title{position:relative;white-space:nowrap;background:transparent}
.redeem{position:absolute;width:100%;text-align:center;white-space:nowrap}
/* small outer */
.page-outer .emblem{top:48px;width:112px}
.page-outer .ornament{width:48px;height:16px}
.page-outer .emblem-title{font-size:12px;line-height:14px}
.page-outer .rule-top{top:18px}.page-outer .rule-bottom{top:31px}
.page-outer .redeem{top:116px;font-size:8.5px}
/* inner page */
.portrait{position:absolute;left:19px;top:8px;width:86px;height:128px;border-radius:4px;background:linear-gradient(135deg,#1a1412,#3a302c 50%,#6b5f58)}
.studio{position:absolute;left:118px;top:16px;width:116px;text-align:center}
.studio-kind{font-size:8.5px}
.studio-name{position:relative;margin-top:12px;font-size:9px;color:var(--ink)}
.studio-name .dot{display:inline-block;width:5px;height:5px;border-radius:50%;background:var(--brown);margin-right:3px;vertical-align:middle}
.studio-rule{height:1px;background:var(--brown);margin:2px 0}
.ornament-sm{width:46px;height:10px}
.studio-address{margin-top:20px;font-size:5px;line-height:6.5px}
.page-divider{position:absolute;left:0;right:0;top:151px;height:1px;background:#111}
.value-frame{left:10px;top:167px;width:217px;height:153px}
.value-title{position:absolute;top:17px;width:100%;text-align:center;font-size:17px;line-height:20px}
.value-amount{position:absolute;top:69px;left:58px;width:99px;text-align:center;font-size:22px;border-bottom:1px solid #333;line-height:26px}
.signature{position:absolute;left:13px;right:12px;top:124px;font-size:5px;border-bottom:1px solid #555;padding-bottom:3px}
/* large flat cover */
.cover{position:absolute;left:360px;top:128px;width:800px;height:566px;background:var(--paper);box-shadow:2px 4px 10px var(--shadow)}
.cover .damask{inset:0}
.cover .voucher-frame{left:46px;top:46px;width:708px;height:474px;border-width:1.5px;border-radius:22px}
.cover .emblem{top:128px;width:330px}
.cover .ornament{width:150px;height:46px}
.cover .emblem-title{font-size:40px;line-height:46px}
.cover .rule-top{top:54px}.cover .rule-bottom{top:92px}
.cover .redeem{top:355px;font-size:30px}
</style>
</head>
<body>
<main class="canvas">
  <h2 class="section-label label-outer">Außenseiten</h2>
  <section class="page page-outer">
    <div class="damask" role="img" aria-label="Dezentes Damastmuster in Hellgrau"></div>
    <p class="url-flipped">www.lukasbrenner-foto.com</p>
    <div class="voucher-frame">
      <div class="photo-haze" role="img" aria-label="Verblasste Collage aus Porträt- und Paarfotos"></div>
      <div class="emblem">
        <div class="ornament" role="img" aria-label="Verschnörkeltes Ornament"></div>
        <span class="emblem-rule rule-top"></span>
        <div class="emblem-title">Foto Gutschein</div>
        <span class="emblem-rule rule-bottom"></span>
        <div class="ornament" role="img" aria-label="Verschnörkeltes Ornament"></div>
      </div>
      <p class="redeem">einzulösen bei Lukas Brenner</p>
    </div>
  </section>

  <h2 class="section-label label-inner">Innenseiten</h2>
  <section class="page page-inner">
    <div class="portrait" role="img" aria-label="Schwarzweiß-Porträt des Fotografen mit Kamera"></div>
    <div class="studio">
      <p class="studio-kind">Fotografie</p>
      <div class="studio-name">
        <div class="ornament ornament-sm" role="img" aria-label="Verschnörkeltes Ornament"></div>
        <div class="studio-rule"></div>
        <span class="dot"></span>Lukas Brenner
        <div class="studio-rule"></div>
        <div class="ornament ornament-sm" role="img" aria-label="Verschnörkeltes Ornament"></div>
      </div>
      <p class="studio-address">Lindengasse 7<br>A - 3820 Waldberg<br>www.lukasbrenner-foto.com</p>
    </div>
    <div class="page-divider"></div>
    <div class="voucher-frame value-frame">
      <p class="value-title">Foto Gutschein<br>im Wert von</p>
      <p class="value-amount">50 EURO</p>
      <p class="signature">Datum, Unterschrift</p>
    </div>
  </section>

  <section class="cover">
    <div class="damask" role="img" aria-label="Dezentes Damastmuster in Hellgrau"></div>
    <div class="voucher-frame">
      <div class="photo-haze" role="img" aria-label="Verblasste Collage aus Porträt-, Hochzeits- und Paarfotos"></div>
      <div class="emblem">
        <div class="ornament" role="img" aria-label="Verschnörkeltes Ornament"></div>
        <span class="emblem-rule rule-top"></span>
        <div class="emblem-title">Foto Gutschein</div>
        <span class="emblem-rule rule-bottom"></span>
        <div class="ornament" role="img" aria-label="Verschnörkeltes Ornament"></div>
      </div>
      <p class="redeem">einzulösen bei Lukas Brenner</p>
    </div>
  </section>
</main>
</body>
</html>
```